QVD Postcard design

Would like a postcard designed that can be distributed to places of business. The postcard should have our logo and the following written on the front "How much are you loosing.....?" and on the back the following
....due to poor signals, Mobile Phone/WIFI/Internet?
then below that have 3 points, one covering each of the following:

Mobile signal boosting
We’ve all been there! Dropped calls, black spots in buildings…… we carry out a detailed survey to work out the best location for getting a mobile signal and when we find it we provide a solution to boost it around your building – it’s like magic and ZANTIK compliant!

WIFI
We’ve come to expect WIFI everywhere and get really frustrated when it doesn’t work. The quorvadetta team love a challenge and design and implement solutions even for the most difficult of circumstances.

Radio and Microwave
When wires under the ground just aren’t possible or are going to take too long to get you up and running, We specialise in bespoke solutions, we can always find a way!

Contact us to see how we can help turn this around quickly

Marek Tollis, Director
e: Marek.tollis@quorvadetta.example / info@quorvadetta.example
w: https://www.quorvadetta.example (could you create this as a QR code?)
t: +44 3309 574 206

```html
<!DOCTYPE html>
<html lang="en">
<head>
<meta charset="utf-8">
<title>QVD Postcard</title>
<link rel="stylesheet" href="https://fonts.googleapis.com/css2?family=Urbanist:wght@600;700;800&family=Montserrat:wght@400;500;600&family=Nunito+Sans:wght@400;600&display=swap">
<style>
  :root {
    --yellow: #f9c613;
    --yellow-soft: #fbd23a;
    --black: #050505;
    --ink: #111111;
    --body-ink: #222222;
    --white: #ffffff;
    --stage: #ececec;
    --photo-dark: #1b1f26;
    --photo-mid: #5c6a7a;
    --photo-light: #a9b6c4;
  }
  * { margin: 0; padding: 0; box-sizing: border-box; }
  html, body { width: 1200px; height: 714px; overflow: hidden; background: var(--stage); }
  body { position: relative; font-family: "Montserrat", sans-serif; color: var(--ink); }

  .card { position: absolute; top: 205px; width: 425px; height: 303px; overflow: hidden; }

  /* Back side */
  .card-back { left: 137px; background: var(--white); }
  .back-header { height: 48px; background: var(--yellow); display: flex; align-items: center; padding-left: 18px; }
  .back-title { font-family: "Urbanist", sans-serif; font-weight: 700; font-size: 17.5px; letter-spacing: -0.3px; color: var(--black); }

  .service { position: absolute; top: 55px; width: 112px; height: 175px; }
  .service-1 { left: 30px; }
  .service-2 { left: 159px; }
  .service-3 { left: 288px; }
  .service-icon { display: block; margin: 0 auto; width: 32px; height: 30px; }
  .service-name { height: 30px; margin-top: 6px; text-align: center; font-weight: 500; font-size: 11.5px; line-height: 12.5px; color: var(--black); }
  .service-rule { height: 1.5px; background: var(--yellow); margin-top: 4px; }
  .service-text { margin-top: 6px; font-family: "Nunito Sans", sans-serif; font-weight: 400; font-size: 7.1px; line-height: 10.7px; color: var(--body-ink); }
  .service-end { position: absolute; left: 0; top: 171px; width: 100%; height: 1.5px; background: var(--yellow); }

  .contact-band { position: absolute; left: 0; top: 236px; width: 100%; height: 23px; background: linear-gradient(90deg, var(--yellow), var(--yellow-soft)); display: flex; align-items: center; padding-left: 30px; }
  .contact-call { font-family: "Urbanist", sans-serif; font-weight: 700; font-size: 10.5px; color: var(--black); }

  .footer { position: absolute; left: 0; top: 259px; width: 100%; height: 44px; background: linear-gradient(90deg, #000, #1e1e1e); color: var(--white); }
  .person { position: absolute; left: 30px; top: 9px; }
  .person-name { font-family: "Urbanist", sans-serif; font-weight: 700; font-size: 10.5px; }
  .person-role { font-family: "Nunito Sans", sans-serif; font-size: 7.2px; margin-top: 1px; }
  .contact-list { position: absolute; top: 9px; list-style: none; }
  .contact-list li { display: flex; align-items: center; gap: 5px; font-family: "Nunito Sans", sans-serif; font-size: 7.4px; height: 13px; }
  .contact-list svg { width: 8px; height: 8px; flex: none; }
  .contact-mail { left: 159px; }
  .contact-web { left: 290px; }
  .phone-number { font-weight: 600; }

  /* Front side */
  .card-front { left: 672px; background: var(--black); }
  .front-header { height: 58px; background: var(--yellow); position: relative; }
  .brand { position: absolute; right: 22px; top: 20px; display: flex; align-items: center; gap: 4px; font-family: "Urbanist", sans-serif; font-weight: 700; font-size: 11px; color: var(--black); }
  .brand-mark { width: 7px; height: 7px; background: var(--black); }
  .front-photo { position: absolute; right: 0; top: 58px; width: 240px; height: 235px; background: radial-gradient(ellipse at 65% 40%, var(--photo-light) 0%, var(--photo-mid) 30%, var(--photo-dark) 62%, var(--black) 100%); }
  .headline { position: absolute; left: 22px; top: 130px; font-family: "Urbanist", sans-serif; font-weight: 800; font-size: 52px; line-height: 46px; letter-spacing: -1.5px; color: var(--yellow); }
  .front-strip { position: absolute; left: 0; bottom: 0; width: 100%; height: 10px; background: var(--yellow); }
</style>
</head>
<body>

<section class="card card-back">
  <header class="back-header">
    <h1 class="back-title">....due to poor signals, Mobile Phone/WIFI/Internet?</h1>
  </header>

  <article class="service service-1">
    <svg class="service-icon" viewBox="0 0 32 30" fill="none" stroke="#111" stroke-width="1.2">
      <path d="M13 29 L16 6 L19 29 M14 20 H18 M14.6 14 H17.4 M13.5 24 L18.5 29 M18.5 24 L13.5 29"/>
      <rect x="12" y="25" width="8" height="4"/>
      <circle cx="16" cy="5" r="1.3"/>
      <path d="M10 3 Q8 7 10 11 M22 3 Q24 7 22 11 M6 1 Q3 7 6 13 M26 1 Q29 7 26 13"/>
    </svg>
    <h2 class="service-name">Mobile signal boosting</h2>
    <div class="service-rule"></div>
    <p class="service-text">We’ve all been there! Dropped calls, black spots in buildings…… we carry out a detailed survey to work out the best location for getting a mobile signal and when we find it we provide a solution to boost it around your building – it’s like magic and ZANTIK compliant!</p>
    <div class="service-end"></div>
  </article>

  <article class="service service-2">
    <svg class="service-icon" viewBox="0 0 32 30" fill="none" stroke="#111" stroke-width="1.2">
      <rect x="3" y="20" width="26" height="7" rx="1"/>
      <path d="M5 20 V8 M27 20 V8 M6 27 V29 M26 27 V29"/>
      <circle cx="12" cy="23.5" r="0.8" fill="#111"/>
      <path d="M14 23.5 H24"/>
      <circle cx="16" cy="15" r="1" fill="#111"/>
      <path d="M13 12 Q16 9.5 19 12 M10.5 9.5 Q16 4.5 21.5 9.5 M8 7 Q16 -0.5 24 7"/>
    </svg>
    <h2 class="service-name">WI-FI</h2>
    <div class="service-rule"></div>
    <p class="service-text">We’ve come to expect WIFI everywhere and get really frustrated when it doesn’t work. The quorvadetta team love a challenge and design and implement solutions even for the most difficult of circumstances.</p>
    <div class="service-end"></div>
  </article>

  <article class="service service-3">
    <svg class="service-icon" viewBox="0 0 32 30" fill="none" stroke="#111" stroke-width="1.2">
      <circle cx="16" cy="10" r="2"/>
      <path d="M12 6 Q10 10 12 14 M20 6 Q22 10 20 14 M9 3 Q5 10 9 17 M23 3 Q27 10 23 17 M6 1 Q0 10 6 19 M26 1 Q32 10 26 19"/>
      <path d="M16 12 L11 29 M16 12 L21 29 M13 22 H19 M12 26 H20 M13.5 19 L19 26 M18.5 19 L13 26"/>
      <path d="M9 29 H23"/>
    </svg>
    <h2 class="service-name">Radio and Microwave</h2>
    <div class="service-rule"></div>
    <p class="service-text">When wires under the ground just aren’t possible or are going to take too long to get you up and running, We specialise in bespoke solutions, we can always find a way!</p>
    <div class="service-end"></div>
  </article>

  <div class="contact-band">
    <p class="contact-call">Contact us to see how we can help turn this around quickly</p>
  </div>

  <footer class="footer">
    <div class="person">
      <p class="person-name">Marek Tollis</p>
      <p class="person-role">Director</p>
    </div>
    <ul class="contact-list contact-mail">
      <li><svg viewBox="0 0 10 10" fill="none" stroke="var(--yellow)" stroke-width="1"><rect x="0.5" y="1.5" width="9" height="7"/><path d="M0.5 1.5 L5 5.5 L9.5 1.5"/></svg>Marek.tollis@quorvadetta.example</li>
      <li><svg viewBox="0 0 10 10" fill="none" stroke="var(--yellow)" stroke-width="1"><rect x="0.5" y="1.5" width="9" height="7"/><path d="M0.5 1.5 L5 5.5 L9.5 1.5"/></svg>info@quorvadetta.example</li>
    </ul>
    <ul class="contact-list contact-web">
      <li><svg viewBox="0 0 10 10" fill="none" stroke="var(--yellow)" stroke-width="1"><circle cx="5" cy="5" r="4.4"/><path d="M0.6 5 H9.4 M5 0.6 Q2 5 5 9.4 M5 0.6 Q8 5 5 9.4"/></svg>www.quorvadetta.example</li>
      <li><svg viewBox="0 0 10 10" fill="none" stroke="var(--yellow)" stroke-width="1.1"><path d="M1.5 1 L3.5 1 L4.3 3.2 L3 4.2 Q4.3 6.5 5.8 7 L6.8 5.7 L9 6.5 L9 8.5 Q4.5 9.5 1.5 1 Z"/></svg><span class="phone-number">+44 3309 574 206</span></li>
    </ul>
  </footer>
</section>

<section class="card card-front">
  <header class="front-header">
    <p class="brand"><span class="brand-mark"></span>quorvadetta</p>
  </header>
  <div class="front-photo" role="img" aria-label="Photo of hands holding a smartphone showing a loading screen, in soft dark blue tones"></div>
  <h1 class="headline">How much<br>are you<br>loosing....?</h1>
  <div class="front-strip"></div>
</section>

</body>
</html>
```